The Brightwater Compass Business Card

We need an attractive business card with the logo that we bought from ArtVantly last year.
Our mission is to contribute to change the way today's leaders manage business companies bringing value to the workplace and helping them to build a new model of creating wealth.
Our logo is clear about our values : we seek Positive Change through People and are convinced that the pursuit of individual well-being and the chase of economic results can converge with the right management.
Management Consulting
Corinne Fabrelle
+34 612 98 70 31
corinne.fabrelle@thebrightwatercompass-mail.net
www.thebrightwatercompass-mail.net

```html
<!DOCTYPE html>
<html lang="en">
<head>
<meta charset="utf-8">
<title>The Brightwater Compass – Business Card</title>
<link rel="stylesheet" href="https://fonts.googleapis.com/css2?family=Tinos:wght@400;700&display=swap">
<style>
  :root {
    --teal-deep: #0b6461;
    --teal-edge: #08524f;
    --teal-light: #80cdc4;
    --paper: #ffffff;
    --backdrop: #dcdcdc;
    --ink-dark: #1d3b3a;
  }
  * { margin: 0; padding: 0; box-sizing: border-box; }
  html, body {
    width: 1200px; height: 1200px; overflow: hidden;
    background: var(--backdrop);
    font-family: "Tinos", "Times New Roman", serif;
  }
  .card {
    position: absolute; left: 170px;
    width: 860px; height: 516px;
    overflow: hidden;
    box-shadow: 0 6px 18px rgba(0,0,0,0.18);
  }
  .card--front { top: 44px; }
  .card--back { top: 640px; background: var(--teal-deep); }
  .card-shapes { position: absolute; inset: 0; }

  .wordmark {
    position: absolute;
    text-transform: uppercase;
    text-align: center;
    font-weight: 400;
    letter-spacing: 2px;
    line-height: 1.15;
  }
  .card--front .wordmark {
    left: 22px; width: 300px; top: 250px;
    font-size: 25px; color: var(--teal-deep);
  }
  .card--back .wordmark {
    left: 0; right: 0; top: 218px;
    font-size: 42px; color: var(--paper);
  }
  .wordmark-dot {
    position: absolute; left: 50%; top: 160px;
    width: 26px; height: 26px; margin-left: -13px;
    border-radius: 50%; background: var(--paper);
  }

  .person {
    position: absolute; right: 44px; top: 96px; text-align: right;
    color: var(--paper);
  }
  .person-name {
    font-size: 36px; text-transform: uppercase; font-weight: 400; letter-spacing: 0.5px;
  }
  .person-name strong { font-weight: 700; }
  .person-title { font-size: 19px; margin-top: 2px; }

  .contacts { position: absolute; right: 47px; top: 288px; list-style: none; }
  .contact {
    display: flex; align-items: center; justify-content: flex-end;
    height: 36px; margin-bottom: 32px;
    font-size: 20px; color: var(--ink-dark);
  }
  .contact svg { width: 36px; height: 36px; margin-left: 14px; flex: none; }

  .back-url {
    position: absolute; left: 0; right: 0; top: 448px;
    text-align: center; font-size: 20px; color: var(--paper);
  }
</style>
</head>
<body>

<section class="card card--front" aria-label="Business card front">
  <svg class="card-shapes" viewBox="0 0 860 516" aria-hidden="true">
    <rect width="860" height="516" fill="var(--teal-light)"/>
    <rect width="860" height="255" fill="var(--teal-deep)"/>
    <polygon points="0,0 229,0 401,255 220,516 0,516" fill="var(--teal-edge)"/>
    <polygon points="0,0 217,0 389,255 208,516 0,516" fill="var(--paper)"/>
  </svg>

  <div class="wordmark">The Brightwater<br>Compass</div>

  <div class="person">
    <h1 class="person-name"><strong>Corinne</strong> Fabrelle</h1>
    <p class="person-title">Managing Director</p>
  </div>

  <ul class="contacts">
    <li class="contact">+34 612 98 70 31
      <svg viewBox="0 0 36 36" aria-hidden="true">
        <polygon points="9,2 27,2 35,18 27,34 9,34 1,18" fill="var(--teal-deep)"/>
        <path d="M12 10c1-1 2-1 3 0l2 3c.5 1 0 2-1 2.5 1 2 2.5 3.5 4.5 4.5.5-1 1.5-1.5 2.5-1l3 2c1 1 1 2 0 3l-1.5 1.5C20 26 10 16 10.5 11.5z" fill="var(--paper)"/>
      </svg>
    </li>
    <li class="contact">corinne.fabrelle@thebrightwatercompass-mail.net
      <svg viewBox="0 0 36 36" aria-hidden="true">
        <polygon points="9,2 27,2 35,18 27,34 9,34 1,18" fill="var(--teal-deep)"/>
        <rect x="9" y="12" width="18" height="12" fill="none" stroke="var(--paper)" stroke-width="1.8"/>
        <polyline points="9,12 18,19 27,12" fill="none" stroke="var(--paper)" stroke-width="1.8"/>
      </svg>
    </li>
    <li class="contact">www.thebrightwatercompass-mail.net
      <svg viewBox="0 0 36 36" aria-hidden="true">
        <polygon points="9,2 27,2 35,18 27,34 9,34 1,18" fill="var(--teal-deep)"/>
        <g fill="none" stroke="var(--paper)" stroke-width="1.6">
          <circle cx="18" cy="18" r="8"/>
          <ellipse cx="18" cy="18" rx="3.5" ry="8"/>
          <line x1="10" y1="18" x2="26" y2="18"/>
        </g>
      </svg>
    </li>
  </ul>
</section>

<section class="card card--back" aria-label="Business card back">
  <span class="wordmark-dot" aria-hidden="true"></span>
  <div class="wordmark">The Brightwater<br>Compass</div>
  <p class="back-url">www.thebrightwatercompass-mail.net</p>
</section>

</body>
</html>
```